Very Simple Web Redesign Project - Using Photoshop

Required is a very simple website home page redesign for the following site: http://www.tallowcrestslate.com.au/
I require this as a Photoshop design.
The basic look and feel of the site needs to remain.
Specifically the colours don't need to be changed.
The positioning of the site is currently correct for the target market.
The site does not need to be made super slick looking. Just upgraded to a new version.
The current text can all be used.
The only menus necessary are a horizontal menu at the top, and a simple horizontal text menu at the bottom of the page. Do NOT retain the vertical menu on the home page (having the items "Our Gallery", "Our Services", "Enquire Now").
Give the horizontal menu the following items:
Home | Slate Roof Repairs | Slate Reroofing | Slate Roof Benefits | Other Services | Photo Gallery | FAQ's | Free Quote | Contact Us
The picture of the house at the top RHS of the page needs to be reduced in size by approx 50% and moved to the top LHS of the page.
Please place the following text into the top of the page:
"Call Now: 0427 618 392"
Keep the four pictures on the home page layout. Some larger images attached.
Thanks,
Rob
Updates
Hi,
Thanks for all the designs.
I am working with my client to get which one they like the most.
Thanks,
Rob

```html
<!DOCTYPE html>
<html lang="en">
<head>
<meta charset="utf-8">
<title>Tallowcrest Roofing – Home</title>
<link rel="stylesheet" href="https://fonts.googleapis.com/css2?family=Marcellus&family=Arimo:wght@400;700&display=swap">
<style>
  :root{
    --green-deep:#2f6a12;
    --green-mid:#3f8417;
    --green-bright:#56a322;
    --green-text:#3a7d12;
    --bar-top:#f4f4f4;
    --bar-bottom:#dcdcdc;
    --tab-grey:#7a7a7a;
    --panel-top:#2e2e2e;
    --panel-bottom:#050505;
    --link-muted:#6a6a6a;
    --white:#ffffff;
    --ink:#000000;
    --drop-grey:#6f6f6f;
  }
  *{box-sizing:border-box;margin:0;padding:0}
  html,body{width:1200px;height:900px;overflow:hidden}
  body{
    position:relative;
    font-family:"Arimo",Arial,sans-serif;
    background:var(--ink);
    color:var(--white);
  }
  .page{
    position:absolute;left:0;top:0;width:1200px;height:722px;
    background:
      radial-gradient(ellipse 900px 420px at 40px 30px, rgba(255,255,255,.07) 0 60%, transparent 61%),
      repeating-linear-gradient(45deg, rgba(0,0,0,.05) 0 2px, transparent 2px 5px),
      linear-gradient(180deg, var(--green-mid), var(--green-deep) 60%, var(--green-mid));
  }
  .welcome-bar{
    position:absolute;left:0;top:0;width:1200px;height:30px;
    background:linear-gradient(var(--bar-top),var(--bar-bottom));
    box-shadow:0 2px 4px rgba(0,0,0,.35);
  }
  .welcome-tab{
    position:absolute;left:150px;top:0;width:68px;height:30px;
    background:var(--tab-grey);color:var(--white);
    font:bold 11px/30px "Arimo",Arial,sans-serif;text-align:center;
  }
  .welcome-text{
    position:absolute;left:226px;top:0;
    font-size:10.5px;line-height:31px;color:var(--green-text);
  }
  .site-header{position:absolute;left:150px;width:900px;height:66px}
  .brand{
    position:absolute;left:14px;top:6px;
    font-family:"Marcellus",Georgia,serif;font-size:40px;color:var(--white);
  }
  .call{
    position:absolute;right:68px;top:13px;text-align:right;line-height:20px;
  }
  .call-label{font-weight:bold;font-size:17px}
  .call-number{font-size:19px}
  .house-icon{position:absolute;right:6px;top:6px;width:50px;height:54px;border-radius:6px;
    background:linear-gradient(#4d6b3b,#2d4423)}
  .main-nav{
    position:absolute;left:150px;width:900px;height:30px;border-radius:16px 16px 0 0;
    background:linear-gradient(var(--green-bright),var(--green-mid));
    display:flex;justify-content:center;gap:17px;
    font-size:13px;line-height:32px;
  }
  .main-nav span{color:var(--white)}
  .photo{position:absolute}
  .content{
    position:absolute;left:150px;top:460px;width:900px;height:190px;
    border-radius:0 0 18px 18px;
    background:linear-gradient(var(--panel-top),var(--panel-bottom));
    padding:13px 18px 0 18px;font-size:12px;line-height:14px;
  }
  .content p{margin-bottom:15px}
  .content .muted{color:var(--link-muted)}
  .footer{position:absolute;left:150px;top:660px;width:900px;height:24px;font-size:10px;font-weight:bold}
  .footer-mark{position:absolute;left:10px;top:0;width:24px;height:24px;border-radius:4px;background:#3c5a2e}
  .footer-copy{position:absolute;left:42px;top:7px}

  .preview{position:absolute;left:150px;top:736px;width:900px;height:139px;overflow:hidden;
    background:
      radial-gradient(ellipse 700px 200px at 0 0, rgba(255,255,255,.07) 0 60%, transparent 61%),
      linear-gradient(180deg, var(--green-mid), var(--green-deep));}
  .dropdown{position:absolute;left:606px;top:831px;width:101px}
  .dropdown div{height:25px;margin-bottom:1px;background:var(--drop-grey);font-size:12px;line-height:25px;padding-left:8px}
</style>
</head>
<body>
  <div class="page">
    <div class="welcome-bar">
      <div class="welcome-tab">Welocome!</div>
      <div class="welcome-text">We service all inner city suburbs of Sydney roughly covering an area encompassing Gordon to Epping, Mosman to Bondi, Coogee to Kogarah and Kingsgrove to Burwood and Concord</div>
    </div>

    <header class="site-header" style="top:32px">
      <div class="brand">Tallowcrest Roofing</div>
      <div class="call"><div class="call-label">Call Now for a free quote</div><div class="call-number">0427 618 392</div></div>
      <div class="house-icon" role="img" aria-label="Small house illustration"></div>
    </header>

    <nav class="main-nav" style="top:95px">
      <span>Home</span><span>Slate Roof Repairs</span><span>Slate Reroofing</span><span>Slate Roof Benefits</span><span>Other Services</span><span>Photo Gallery</span><span>FAQ's</span><span>Free Quote</span><span>Contact Us</span>
    </nav>

    <div class="photo" style="left:150px;top:125px;width:390px;height:335px;background:linear-gradient(160deg,#5b5f62,#7d6a5f 45%,#b9b8b0)" role="img" aria-label="Photo of a Victorian house with a slate roof and white gable trim"></div>
    <div class="photo" style="left:540px;top:125px;width:180px;height:335px;background:linear-gradient(170deg,#8c8a86,#4e4a5a 40%,#3b3745)" role="img" aria-label="Photo of a dormer window in a new slate roof"></div>
    <div class="photo" style="left:720px;top:125px;width:330px;height:168px;background:linear-gradient(160deg,#8a5a4a,#5c6366 40%,#6f7470)" role="img" aria-label="Photo of a low slate roof against a brick wall"></div>
    <div class="photo" style="left:720px;top:293px;width:330px;height:167px;background:linear-gradient(170deg,#4e7a36,#6a6156 55%,#4f6a33)" role="img" aria-label="Photo of a round gazebo with a conical slate roof among trees"></div>

    <section class="content">
      <p>At Tallowcrest Roofing we specialize in the upkeep, maintenance, repair and replacement of all types of slate roof as well as wood shingles.&nbsp; We can track down the leak that just won't go away or give your house a complete re-roof. We can also provide all your guttering needs.</p>
      <p>Tallowcrest Roofing is a small company and as such we do not have the overheads that larger companies do.&nbsp; Quality work and attention to detail are our trademark.</p>
      <p>All photos on this website consist of work which I have personally done.&nbsp; The above photos provide at a quick glance a reasonable cross section of the type of work I do.</p>
      <p>By clicking on the <span class="muted">Photo Gallery</span> link you can see other work including some before and after shots.</p>
      <p>Feel free to call at your earliest convenience to organise an obligation free quote or fill out a form by clicking on the <span class="muted">Contact Us</span> link below.</p>
    </section>

    <footer class="footer">
      <div class="footer-mark" role="img" aria-label="Small house illustration"></div>
      <div class="footer-copy">© 2009 Tallowcrest Roofing</div>
    </footer>
  </div>

  <div class="preview">
    <header class="site-header" style="top:0;left:0">
      <div class="brand">Tallowcrest Roofing</div>
      <div class="call"><div class="call-label">Call Now for a free quote</div><div class="call-number">0427 618 392</div></div>
      <div class="house-icon" role="img" aria-label="Small house illustration"></div>
    </header>
    <nav class="main-nav" style="top:64px;left:0">
      <span>Home</span><span>Slate Roof Repairs</span><span>Slate Reroofing</span><span>Slate Roof Benefits</span><span>Other Services</span><span>Photo Gallery</span><span>FAQ's</span><span>Free Quote</span><span>Contact Us</span>
    </nav>
    <div class="photo" style="left:0;top:95px;width:900px;height:44px;background:linear-gradient(90deg,#4f6a36,#6d6f72 35%,#5d6066 70%,#6f7a3a)" role="img" aria-label="Photo strip of slate roofs"></div>
  </div>

  <div class="dropdown">
    <div>Our Services</div>
    <div>Fact File</div>
  </div>
</body>
</html>
```